Brightwire Hollow Business cards

one side I would like my logo (uploaded) and the other side I want my details. I'm an electrician in sydney. The logo side I'm happy with just a white background and our logo in the middle.

Details for other side
24/7 Sydney Electrician
Marcus Pell
0431 587 219
marcus@brightwirehollow.com.au
brightwirehollow.com.au
icons for facebook, instagram, linked in

Industry/Entity Type

electrician

Contact Information for Business Card

company info

```html
<!DOCTYPE html>
<html lang="en">
<head>
<meta charset="utf-8">
<title>Brightwire Hollow — Business Cards</title>
<link rel="stylesheet" href="https://fonts.googleapis.com/css2?family=Montserrat:wght@500;700;800&family=Lato:wght@400;700&display=swap">
<style>
  :root {
    --stage: #1a1a1b;
    --card: #262628;
    --red: #ec3324;
    --white: #ffffff;
    --muted: #e8e8e8;
  }
  * { box-sizing: border-box; margin: 0; padding: 0; }
  html, body { width: 1200px; height: 952px; overflow: hidden; background: var(--stage); }
  .canvas {
    width: 1200px; height: 952px;
    display: flex; flex-direction: column; align-items: center; justify-content: center; gap: 40px;
  }
  .card {
    position: relative; width: 700px; height: 400px;
    background: var(--card); overflow: hidden;
    box-shadow: 0 12px 30px rgba(0,0,0,.45);
  }
  /* Details side */
  .card__mark {
    position: absolute; left: 0; top: 0; width: 300px; height: 280px;
    background: var(--red);
    border-bottom-right-radius: 140px;
  }
  .card__name {
    position: absolute; left: 330px; top: 60px;
    font-family: "Montserrat", sans-serif; font-size: 40px; line-height: 1.1;
    color: var(--white); text-transform: uppercase; letter-spacing: 1px;
  }
  .card__name .first { font-weight: 500; display: block; }
  .card__name .last { font-weight: 700; display: block; }
  .contact-list {
    position: absolute; left: 330px; top: 185px; list-style: none;
    font-family: "Lato", sans-serif; font-size: 17px; color: var(--muted);
  }
  .contact-list li { display: flex; align-items: center; gap: 12px; margin-bottom: 12px; }
  .contact-icon {
    width: 24px; height: 24px; border-radius: 5px; background: var(--red);
    display: flex; align-items: center; justify-content: center; flex: none;
  }
  .social {
    position: absolute; left: 60px; top: 310px; display: flex; gap: 12px;
  }
  .social__item { width: 30px; height: 30px; border-radius: 6px; background: var(--white); }
  .card__tagline {
    position: absolute; left: 60px; top: 355px;
    font-family: "Montserrat", sans-serif; font-weight: 800; font-size: 17px;
    color: var(--white); text-transform: uppercase; letter-spacing: 1px;
  }
  /* Logo side */
  .card--logo { display: flex; align-items: center; justify-content: center; }
  .brand {
    font-family: "Montserrat", sans-serif; font-weight: 800; font-size: 52px;
    color: var(--red); text-transform: uppercase; letter-spacing: 2px;
  }
</style>
</head>
<body>
<main class="canvas">
  <section class="card card--details">
    <div class="card__mark" role="img" aria-label="Large red brand mark"></div>
    <h1 class="card__name"><span class="first">Marcus</span><span class="last">Pell</span></h1>
    <ul class="contact-list">
      <li>
        <span class="contact-icon">
          <svg width="14" height="14" viewBox="0 0 24 24" aria-hidden="true"><path fill="#fff" d="M6.6 10.8a15 15 0 0 0 6.6 6.6l2.2-2.2a1 1 0 0 1 1-.25 11.4 11.4 0 0 0 3.6.57 1 1 0 0 1 1 1V20a1 1 0 0 1-1 1A17 17 0 0 1 3 4a1 1 0 0 1 1-1h3.5a1 1 0 0 1 1 1c0 1.25.2 2.45.57 3.57a1 1 0 0 1-.25 1z"/></svg>
        </span>0431 587 219
      </li>
      <li>
        <span class="contact-icon">
          <svg width="14" height="14" viewBox="0 0 24 24" aria-hidden="true"><rect x="3" y="6" width="18" height="12" rx="1" fill="none" stroke="#fff" stroke-width="2"/><path d="M3 7l9 6 9-6" fill="none" stroke="#fff" stroke-width="2"/></svg>
        </span>marcus@brightwirehollow.com.au
      </li>
      <li>
        <span class="contact-icon">
          <svg width="14" height="14" viewBox="0 0 24 24" aria-hidden="true"><circle cx="12" cy="12" r="9" fill="none" stroke="#fff" stroke-width="2"/><path d="M3 12h18M12 3c3 3 3 15 0 18M12 3c-3 3-3 15 0 18" fill="none" stroke="#fff" stroke-width="1.6"/></svg>
        </span>brightwirehollow.com.au
      </li>
    </ul>
    <div class="social" aria-label="Social links">
      <span class="social__item"></span>
      <span class="social__item"></span>
      <span class="social__item"></span>
    </div>
    <p class="card__tagline">24/7 Sydney Electrician</p>
  </section>

  <section class="card card--logo">
    <p class="brand">Brightwire Hollow</p>
  </section>
</main>
</body>
</html>
```